South Florida Real Estate Brokerage Business

The name is HOME CALVINA REAL ESTATE.
The company is a Real estate realty based in Miami.
Is targeted to Latin American clients.
Must express luxury, and efficiency.
Target clients for properties around 250k to a million +.
Calvina means Royal in Latin.
Should communicate safety and knowledge of the product and transaction with a tech edge.

The web design needs to be a Social tool, with Friendlane and other media integration of some sort. Needs to have a Show case place, a Search place (MLS listings) with maps and filters.
Needs to reflect luxury but also mixed with a social edge capable of engaging clients or transition them to communicate with the page.
Include the logo from the uploaded files, feel free to change the color or font per webdesign.
This is a Front en design, layout and graphics.
Possible future programming if approved.
I can receive Quotes for the Code part.

Target Market(s)

Spanish and English speakers living in Latin America and Canada looking for apartments and houses to buy.

Industry/Entity Type

Business

Requirements
Must have
• Search area.
Neighbourhood area.
Could be a blog or news area.
Client registration.
Social Plugin
Nice to have
• Social linking to networks.
Log in with friendlane account.
Friendlane Like.

```html
<!DOCTYPE html>
<html lang="en">
<head>
<meta charset="utf-8">
<title>Home Calvina Real Estate</title>
<link href="https://fonts.googleapis.com/css2?family=Didact+Gothic&family=PT+Sans:wght@400;700&display=swap" rel="stylesheet">
<style>
:root{
  --gold:#c89a4a;
  --gold-dark:#a8762c;
  --ink:#222;
  --muted:#555;
  --page:#ebebeb;
  --dark:#2a2623;
  --dark-2:#1d1a18;
  --panel:rgba(40,34,28,.88);
  --line:#ddd;
}
*{box-sizing:border-box;margin:0;padding:0}
html,body{width:1040px;height:1200px;overflow:hidden}
body{position:relative;background:var(--page);font-family:"PT Sans",sans-serif;font-size:10px;color:var(--ink)}
.abs{position:absolute}
h2{font-family:"Didact Gothic",sans-serif;font-weight:400;font-size:14px;color:var(--ink);white-space:nowrap}
h2 em{font-style:normal;color:var(--gold)}
.gold{color:var(--gold)}
.btn{position:absolute;background:linear-gradient(#d3a85b,#a8762c);color:#fff;font-size:9px;text-align:center;border-radius:1px}
/* header */
.topbar{left:0;top:0;width:1040px;height:77px;background:#fff}
.logo-disc{left:100px;top:20px;width:176px;height:92px;background:#fff;border-radius:50%}
.logo-mark{left:165px;top:12px;width:44px;height:44px;background:var(--gold)}
.logo-name{left:104px;top:62px;width:168px;text-align:center;font-family:"Didact Gothic",sans-serif;color:#333;font-size:18px;letter-spacing:.5px}
.logo-sub{left:104px;top:83px;width:168px;text-align:center;font-family:"Didact Gothic",sans-serif;color:#333;font-size:9px;letter-spacing:1px}
.client-reg{left:712px;top:10px;font-size:8px;color:#888}
.client-reg:before{content:"▸ ";color:var(--gold)}
.signin{left:807px;top:8px;width:120px;height:17px;background:#3b5c9a;color:#fff;font-size:8px;font-weight:700;line-height:17px;padding-left:22px;border-radius:2px}
.signin:before{content:"";position:absolute;left:6px;top:4px;width:9px;height:9px;background:#fff;border-radius:1px}
.nav{left:278px;top:47px;font-family:"Didact Gothic",sans-serif;font-size:10px;color:#555}
.nav span{position:absolute;white-space:nowrap}
.nav .on{color:#222;border-bottom:2px solid var(--gold);padding:0 12px 5px}
/* hero */
.hero-band{left:0;top:77px;width:1040px;height:340px;background:var(--dark)}
.hero-photo{left:107px;top:77px;width:819px;height:340px;background:linear-gradient(90deg,#8c7a5a 0%,#c9b38a 30%,#8d6b3e 55%,#5c4a33 80%,#3b2f24 100%)}
.tagline{left:127px;top:310px;width:304px;height:87px;background:rgba(30,26,22,.72);padding:16px 18px;font-family:"Didact Gothic",sans-serif;font-size:20px;line-height:26px;color:#fff;white-space:nowrap}
.search{left:683px;top:77px;width:221px;height:340px;background:var(--panel);color:var(--gold)}
.search h3{position:absolute;left:22px;top:20px;font-family:"Didact Gothic",sans-serif;font-weight:400;font-size:13.5px;color:#fff;white-space:nowrap}
.search label{position:absolute;font-size:8px}
.sel{position:absolute;height:23px;background:#1f1b18;border:1px solid #5a4a33;color:#999;font-size:8px;line-height:21px;padding-left:8px}
.sel:after{content:"";position:absolute;right:0;top:0;width:22px;height:21px;border-left:1px solid #3a322a}
.sel i{position:absolute;right:7px;top:9px;width:0;height:0;border-left:4px solid transparent;border-right:4px solid transparent;border-top:4px solid #ddd;z-index:1}
.search .hint{position:absolute;left:0;top:318px;width:221px;text-align:center;font-size:8px;color:#aaa}
/* cards */
.card{background:#fff}
.rule{position:absolute;height:1px;background:var(--line)}
.body-txt{font-size:9.5px;color:#444;line-height:12px}
.thumb{left:404px;top:472px;width:84px;height:44px;background:linear-gradient(#4d6e8a,#9bb3a0 55%,#e9e4da 60%,#5f7a45);border:1px solid #ccc}
.field{position:absolute;border:1px solid #ddd;background:#fff;color:#bbb;font-style:italic;font-size:9px;padding:5px 8px}
.list{position:absolute;list-style:none;font-size:9.5px;line-height:16px;white-space:nowrap}
.list li:before{content:"▸ ";color:var(--gold);font-size:7px}
.tweet{position:absolute;left:684px;width:218px;font-size:9.5px;line-height:13px;padding-bottom:4px;border-bottom:1px dashed #ccc}
.tweet small{display:block;font-size:8px;color:#999;line-height:10px}
/* footer */
.footer{left:0;top:898px;width:1040px;height:302px;background:var(--dark);border-top:2px solid var(--gold)}
.footer h2{color:#fff}
.f-txt{font-size:9.5px;line-height:13px;color:#8e8a84}
.f-rule{position:absolute;height:1px;background:#403a35}
.soc{position:absolute;top:1002px;width:18px;height:18px;background:#eee}
.url{left:371px;top:1032px;width:234px;height:26px;background:var(--dark-2);border-radius:3px;color:#999;font-size:9.5px;line-height:26px;padding-left:10px}
.in{position:absolute;width:174px;height:24px;background:#1e1a17;border:1px solid #54442f;color:#999;font-size:8.5px;line-height:22px;padding-left:8px}
.req{position:absolute;font-size:8.5px;color:var(--gold)}
</style>
</head>
<body>

<header>
  <div class="abs topbar"></div>
  <div class="abs hero-band"></div>
  <div class="abs hero-photo" role="img" aria-label="Photo of a luxury bedroom with arched window and mountain view"></div>
  <div class="abs logo-disc"></div>
  <div class="abs logo-mark"></div>
  <div class="abs logo-name">HOME CALVINA</div>
  <div class="abs logo-sub">REAL ESTATE</div>
  <div class="abs client-reg">Client Registration</div>
  <div class="abs signin">Sign in with Friendlane</div>
  <nav class="abs nav">
    <span class="on" style="left:0">HOME</span>
    <span style="left:75px">MIAMI CONDOS</span>
    <span style="left:185px">NEIGHBORHOOD</span>
    <span style="left:303px">BLOG</span>
    <span style="left:363px">SEARCH</span>
    <span style="left:433px">RENTALS</span>
    <span style="left:504px">MAP SEARCH</span>
    <span style="left:600px">CONTACT</span>
  </nav>
</header>

<div class="abs tagline">South Florida’s Premier Luxury<br><span class="gold">Real Estate</span> Boutique</div>

<form class="abs search">
  <h3>Search for <span class="gold">Calvina Real Estate</span></h3>
  <label style="left:22px;top:53px">Location</label>
  <div class="sel" style="left:22px;top:63px;width:199px;width:177px">All Location<i></i></div>
  <label style="left:22px;top:98px">Type of Property</label>
  <div class="sel" style="left:22px;top:108px;width:177px">All Property<i></i></div>
  <label style="left:22px;top:145px">Bed/s</label>
  <label style="left:116px;top:145px">Bath/s</label>
  <div class="sel" style="left:22px;top:155px;width:83px">Any Num<i></i></div>
  <div class="sel" style="left:116px;top:155px;width:83px">Any Num<i></i></div>
  <label style="left:22px;top:193px">Price from</label>
  <div class="sel" style="left:22px;top:203px;width:177px">$1,000<i></i></div>
  <label style="left:22px;top:239px">Price to</label>
  <div class="sel" style="left:22px;top:249px;width:177px">$10 million<i></i></div>
  <div class="btn" style="left:58px;top:284px;width:105px;height:26px;line-height:26px;font-size:10px">Search Now</div>
  <div class="hint">or try our <span class="gold">Advanced Search</span></div>
</form>

<section class="abs card" style="left:107px;top:417px;width:819px;height:172px"></section>
<h2 class="abs" style="left:127px;top:435px">Home Calvina <em>News</em></h2>
<div class="rule" style="left:127px;top:458px;width:221px"></div>
<div class="abs body-txt" style="left:129px;top:471px;width:225px"><span class="gold">Lorem ipsum dolor sit amet, consectetuer</span><br>Adipiscing elit, sed diam nonummy nibh euismod tincidunt ut laoreet dolore magna</div>
<div class="btn" style="left:130px;top:532px;width:68px;height:20px;line-height:20px">Readmore</div>

<h2 class="abs" style="left:402px;top:435px">Home Calvina <em>Real Estate</em></h2>
<div class="rule" style="left:402px;top:458px;width:246px"></div>
<div class="abs thumb" role="img" aria-label="Photo of a white two-storey house among trees"></div>
<div class="btn" style="left:403px;top:526px;width:86px;height:20px;line-height:20px">Search Listings</div>
<div class="abs body-txt" style="left:501px;top:473px;width:130px"><span class="gold">Lorem ipsum dolor sit amet consectetuer</span><br><span style="color:#222">Adipiscing elit, sed diam nonummy nibh euismod tincidunt ut laoreet dolore magna</span></div>

<h2 class="abs" style="left:683px;top:435px">Email Newsletter</h2>
<div class="rule" style="left:683px;top:458px;width:221px"></div>
<div class="abs body-txt" style="left:685px;top:471px;width:225px">Adipiscing elit, sed diam nonummy nibh euismod tincidunt ut laoreet dolore magna</div>
<div class="field" style="left:683px;top:505px;width:220px;height:21px">Your email here</div>
<div class="btn" style="left:685px;top:536px;width:87px;height:20px;line-height:20px">Subscribe Now</div>

<section class="abs card" style="left:107px;top:601px;width:819px;height:279px"></section>
<h2 class="abs" style="left:127px;top:619px">Neighborhood <em>Area</em></h2>
<div class="abs" style="left:564px;top:623px;font-size:9.5px">Sort by <span class="gold">Name</span></div>
<div class="rule" style="left:127px;top:642px;width:497px"></div>
<ul class="list" style="left:129px;top:652px">
  <li>Allison Islands</li><li>Atlantis</li><li>Aventura</li><li>Bal Harbour</li><li class="gold">Bay Harbor Islands</li><li>Belle Glade</li><li>Biscayne Park</li><li>Biscayne Gardens</li><li>Boca Raton</li><li>Boynton Beach</li>
</ul>
<ul class="list" style="left:257px;top:652px">
  <li>Cloud Lake</li><li>Coconut Creek</li><li>Coconut Grove</li><li>Cooper City</li><li>Coral Gables</li><li>Coral Springs</li><li>Cutler Bay</li><li class="gold">Dania</li><li>Davie</li><li>Deerfield Beach</li>
</ul>
<ul class="list" style="left:369px;top:652px">
  <li>Doral</li><li class="gold">Eastern Shores</li><li>El Portal</li><li>Fisher Island</li><li>Florida City</li><li>Fort Lauderdale</li><li>Fort Pierce</li><li>Golden Beach</li><li>Goulds</li><li>Green Acres</li>
</ul>
<ul class="list" style="left:489px;top:652px">
  <li>Gulf Stream</li><li>Gulf View</li><li>Hallandale</li><li>Hialeah</li><li>Hialeah Gardens</li><li>Star,Palm,Hibiscus Islands</li><li>Highland Beach</li><li>Hillsboro Beach</li><li>Hobe Sound</li><li class="gold">Hollywood</li>
</ul>
<div class="rule" style="left:127px;top:835px;width:497px"></div>
<div class="abs" style="left:130px;top:850px;font-size:9.5px">View neighborhood area using <span class="gold">Map</span></div>
<div class="btn" style="left:558px;top:846px;width:68px;height:19px;line-height:19px">View All</div>

<h2 class="abs" style="left:682px;top:619px">Chirper Feed</h2>
<div class="rule" style="left:682px;top:642px;width:221px"></div>
<div class="tweet" style="top:654px"><span class="gold">@BayviewNora</span> I posted a new photo to Friendlane <span class="gold">http://ch.rp/Qm4tLw8</span><small>6 minutes ago • reply</small></div>
<div class="tweet" style="top:702px"><span class="gold">@BayviewNora</span> I posted a new photo to Friendlane <span class="gold">http://ch.rp/Qm4tLw8</span><small>6 minutes ago • reply</small></div>
<div class="tweet" style="top:750px"><span class="gold">@BayviewNora</span> I posted a new photo to Friendlane <span class="gold">http://ch.rp/Qm4tLw8</span><small>6 minutes ago • reply</small></div>
<div class="tweet" style="top:798px;border:0"><span class="gold">@BayviewNora</span> I posted a new photo to Friendlane <span class="gold">http://ch.rp/Qm4tLw8</span><small>6 minutes ago • reply</small></div>
<svg class="abs" style="left:786px;top:845px" width="8" height="5"><path d="M0 0h8L4 5z" fill="#c89a4a"/></svg>

<footer class="abs footer"></footer>
<h2 class="abs" style="left:106px;top:930px;color:#fff">Speak with our <em>Home Calvina</em> Realtors</h2>
<div class="f-rule" style="left:106px;top:954px;width:219px"></div>
<div class="abs f-txt" style="left:108px;top:966px;width:222px">If you would like to speak with one of our Home Calvina Real Estate agents immediately please call <span style="color:#fff">305-555-0142</span> and our qualified Realtors will be happy to assist you.</div>
<div class="abs" style="left:108px;top:1041px;font-size:9.5px;color:var(--gold)">Office: (305) 555-0142, Toll Free: 800-555-0199</div>

<h2 class="abs" style="left:370px;top:930px;color:#fff">Connect With Us</h2>
<div class="f-rule" style="left:370px;top:954px;width:231px"></div>
<div class="abs f-txt" style="left:373px;top:966px;width:240px">Lorem ipsum dolor sit amet, consectetuer adipiscing elit, sed diam nonummy nibh.</div>
<div class="soc" style="left:374px;background:var(--gold);border-radius:50%"></div>
<div class="soc" style="left:404px;border-radius:50%"></div>
<div class="soc" style="left:444px"></div>
<div class="soc" style="left:486px"></div>
<div class="soc" style="left:527px;border-radius:50%"></div>
<div class="soc" style="left:566px;border-radius:50%"></div>
<div class="abs url">www.friendlane.com/<span class="gold">homecalvinarealestate</span></div>
<div class="abs" style="left:374px;top:1074px;width:36px;height:16px;background:#eef;border:1px solid #8ea0c8;font-size:8px;line-height:14px;padding-left:16px;color:#3b5c9a">Like</div>
<div class="abs" style="left:379px;top:1078px;width:9px;height:9px;background:#3b5c9a"></div>
<div class="abs" style="left:415px;top:1075px;width:20px;height:14px;background:#fff;border:1px solid #ccc;font-size:8px;line-height:12px;text-align:center">17K</div>

<h2 class="abs" style="left:650px;top:930px;color:#fff">Client Login</h2>
<div class="f-rule" style="left:650px;top:954px;width:276px"></div>
<div class="in" style="left:652px;top:968px">Username</div>
<div class="req" style="left:836px;top:975px">* Required</div>
<div class="in" style="left:652px;top:999px">Password</div>
<div class="req" style="left:836px;top:1006px">* Required</div>
<div class="btn" style="left:653px;top:1036px;width:69px;height:22px;line-height:22px;font-size:11px">Login</div>
<div class="abs" style="left:735px;top:1041px;font-size:9.5px;color:#8e8a84">Click <span style="color:#fff">here</span> for forgot your password</div>

<div class="f-rule" style="left:107px;top:1115px;width:751px"></div>
<div class="abs" style="left:0;top:1135px;width:1040px;text-align:center;font-size:8.5px;color:#6f6a64">© 2012 Home Calvina Real Estate. All Rights Reserved. <span class="gold">Listings Site Map</span></div>

</body>
</html>
```